Whole Body Cryotherapy Business needs a Brochure

We need a brochure for marketing events of our spa. The name of the business is FrostHaven. Our website is www.frosthavenspa-example.com. We are located in New York City at the Lindenmark. We need an eye catching brochure that discusses the health benefits of whole body cryotherapy. We need an editable file to be able to tweak the language of the brochure. The contact information that should be on the brochure is as follows:

FrostHaven
Lindenmark, 482 W. 19th Street
New York, NY 10388

Phone: (855) 614-3098

EMail: frosthavenspa@mailbox-example.com

We prefer a color scheme that mainly uses blue, but are open to any design that is eye catching.

We need the brochure to fit on 8.5" x 11" paper.

Requirements
Must have
• Must have space for the following paragraphs (use Lorem Ipsem and we can fill in later): (1) What is Whole Body Cryotherapy and (2) What makes FrostHaven different.

```html
<!DOCTYPE html>
<html lang="en">
<head>
<meta charset="utf-8">
<title>FrostHaven – Freeze Into Fitness</title>
<link rel="stylesheet" href="https://fonts.googleapis.com/css2?family=Montserrat:wght@700&family=Encode+Sans+Semi+Condensed:wght@300&family=Open+Sans:wght@400;600;800&family=Roboto+Condensed:wght@700&family=Fira+Sans+Condensed:wght@700&family=PT+Sans:wght@400;700&display=swap">
<style>
  :root {
    --page-bg: #efefef;
    --sheet-white: #ffffff;
    --ice-light: #e4f2fb;
    --ice-mid: #b9dcf3;
    --ice-deep: #8fc7ea;
    --brand-blue: #0b63b5;
    --brand-blue-dark: #0a4f96;
    --headline-blue: #1565b0;
    --heading-blue: #1a4e9e;
    --panel-border: #8f8cc9;
    --body-ink: #1d1d1d;
    --rule: #c9d3dc;
    --white: #ffffff;
  }
  * { box-sizing: border-box; margin: 0; padding: 0; }
  html, body {
    width: 1001px; height: 1200px; overflow: hidden;
    background: var(--page-bg);
  }
  .flyer {
    position: absolute; left: 57px; top: 27px;
    width: 887px; height: 1146px;
    background:
      radial-gradient(ellipse at 20% 60%, var(--ice-mid) 0%, transparent 55%),
      radial-gradient(ellipse at 80% 95%, var(--ice-deep) 0%, transparent 45%),
      radial-gradient(ellipse at 10% 100%, var(--ice-deep) 0%, transparent 40%),
      linear-gradient(160deg, var(--sheet-white) 0%, var(--ice-light) 45%, var(--ice-mid) 100%);
    overflow: hidden;
    font-family: "PT Sans", sans-serif;
  }
  .hero-photo {
    position: absolute; left: 122px; top: 22px; width: 243px; height: 452px;
    background: linear-gradient(180deg, #c9c9c9 0%, #7c7c7c 18%, #b98a6c 45%, #e6e9ee 75%, #9fa3a8 100%);
    border-radius: 40px 40px 0 0;
  }
  .brand-shield {
    position: absolute; left: 63px; top: 471px; width: 354px; height: 556px;
  }
  .brand-shield svg { position: absolute; inset: 0; }
  .brand-mark {
    position: absolute; left: 124px; top: 24px; width: 106px; height: 106px;
    border: 4px solid var(--white); border-radius: 50%;
  }
  .brand-name {
    position: absolute; left: 0; top: 144px; width: 100%; text-align: center;
    font-family: "Montserrat", sans-serif; font-weight: 700; font-size: 50px;
    color: var(--white); letter-spacing: -0.5px;
  }
  .tagline {
    position: absolute; left: 0; top: 232px; width: 100%; text-align: center;
    font-family: "Encode Sans Semi Condensed", sans-serif; font-weight: 300;
    font-size: 32px; line-height: 41px; color: var(--white);
  }
  .offer {
    position: absolute; left: 0; top: 325px; width: 100%; text-align: center;
    font-family: "Encode Sans Semi Condensed", sans-serif; font-weight: 300;
    font-size: 25px; color: var(--white);
  }
  .website {
    position: absolute; left: 0; top: 410px; width: 100%; text-align: center;
    font-family: "Open Sans", sans-serif; font-weight: 800; font-size: 18px;
    color: var(--white); letter-spacing: 0.3px;
  }
  .phone {
    position: absolute; left: 0; top: 440px; width: 100%; text-align: center;
    font-family: "Roboto Condensed", sans-serif; font-weight: 700; font-size: 35px;
    color: var(--white); letter-spacing: 0.5px;
  }
  .address {
    position: absolute; left: 63px; top: 1040px; width: 354px; text-align: center;
    font-family: "Open Sans", sans-serif; font-size: 15px; line-height: 22px; color: var(--body-ink);
  }
  .address strong { font-weight: 600; }
  .email {
    position: absolute; left: 40px; top: 1088px; width: 400px; text-align: center;
    font-family: "Open Sans", sans-serif; font-size: 18px; color: var(--body-ink);
  }
  .headline {
    position: absolute; left: 470px; top: 62px; width: 352px; text-align: center;
    font-family: "Fira Sans Condensed", sans-serif; font-weight: 700;
    font-size: 66px; line-height: 77px; color: var(--headline-blue);
  }
  .info-panel {
    position: absolute; left: 448px; top: 242px; width: 404px; height: 861px;
    border: 1.5px solid var(--panel-border); border-radius: 30px;
    background: rgba(255,255,255,0.55);
  }
  .info-section { position: absolute; left: 18px; width: 366px; }
  .info-section h2 {
    font-family: "PT Sans", sans-serif; font-weight: 700; font-size: 27px;
    line-height: 33px; color: var(--heading-blue);
  }
  .info-section p {
    margin-top: 13px; font-size: 13.6px; line-height: 18px; color: var(--body-ink);
    text-align: justify; text-align-last: center;
  }
  .section-rule {
    position: absolute; left: 18px; width: 366px; height: 1px; background: var(--rule);
  }
  .benefit-list { list-style: none; margin-top: 10px; }
  .benefit-list li {
    position: relative; padding-left: 18px; font-size: 13.6px; line-height: 20.7px; color: var(--body-ink);
  }
  .benefit-list li::before {
    content: ""; position: absolute; left: 1px; top: 6px; width: 9px; height: 9px; border-radius: 50%;
    background: radial-gradient(circle at 35% 35%, #8f95c8, #2c2f6b);
  }
</style>
</head>
<body>
  <main class="flyer">
    <div class="hero-photo" role="img" aria-label="Photo of a client stepping out of a whole body cryotherapy chamber surrounded by cold mist"></div>

    <section class="brand-shield">
      <svg width="354" height="556" viewBox="0 0 354 556" aria-hidden="true">
        <defs>
          <linearGradient id="shieldFill" x1="0" y1="0" x2="0" y2="1">
            <stop offset="0" stop-color="#0a4f96"/>
            <stop offset="1" stop-color="#0f6fc0"/>
          </linearGradient>
        </defs>
        <path d="M14 0 H340 Q354 0 354 14 V447 L177 556 L0 447 V14 Q0 0 14 0 Z" fill="url(#shieldFill)"/>
      </svg>
      <div class="brand-mark" aria-hidden="true"></div>
      <div class="brand-name">FrostHaven</div>
      <div class="tagline">Wholebody Cryotherapy<br>is coming to NYC</div>
      <div class="offer">Claim your free session</div>
      <div class="website">www.frosthavenspa-example.com</div>
      <div class="phone">(855) 614-3098</div>
    </section>

    <p class="address"><strong>FrostHaven,</strong> Lindenmark, 482 W. 19th Street<br>New York, NY 10388</p>
    <p class="email">frosthavenspa@mailbox-example.com</p>

    <h1 class="headline">FREEZE INTO<br>FITNESS</h1>

    <section class="info-panel">
      <article class="info-section" style="top:12px;">
        <h2>What is Whole Body<br>Cryotherapy</h2>
        <p>Lorem ipsum dolor sit amet, consectetur adipiscing elit, sed do eiusmod tempor incididunt ut labore et dolore magna aliqua. Ut enim ad minim veniam, quis nostrud exercitation ullamco laboris nisi ut aliquip ex ea commodo consequat. Duis aute irure dolor in reprehenderit in voluptate velit esse cillum dolore eu fugiat nulla pariatur. Excepteur sint occaecat cupidatat non proident, sunt in culpa qui officia deserunt mollit anim id est laborum.</p>
      </article>
      <div class="section-rule" style="top:279px;"></div>
      <article class="info-section" style="top:291px;">
        <h2>What makes FrostHaven<br>different</h2>
        <p>Lorem ipsum dolor sit amet, consectetur adipiscing elit, sed do eiusmod tempor incididunt ut labore et dolore magna aliqua. Ut enim ad minim veniam, quis nostrud exercitation ullamco laboris nisi ut aliquip ex ea commodo consequat. Duis aute irure dolor in reprehenderit in voluptate velit esse cillum dolore eu fugiat nulla pariatur. Excepteur sint occaecat cupidatat non proident, sunt in culpa qui officia deserunt mollit anim id est laborum.</p>
      </article>
      <div class="section-rule" style="top:553px;"></div>
      <article class="info-section" style="top:572px;">
        <h2>Health benefits of whole<br>body cryotherapy</h2>
        <ul class="benefit-list">
          <li>Lorem ipsum dolor sit amet, consectetur sit</li>
          <li>Lorem ipsum dolor sit amet, consectetur dolor amet</li>
          <li>Lorem ipsum dolor sit amet, consectetur dolor sit</li>
          <li>Lorem ipsum dolor sit amet, consectetur sit amet</li>
          <li>Lorem ipsum dolor sit amet, consectetur sit amet</li>
          <li>Lorem ipsum dolor sit amet, consectetur dolor sit</li>
          <li>Lorem ipsum dolor sit amet, consectetur sit amet</li>
          <li>Lorem ipsum dolor sit consectetur dolor sit amet</li>
          <li>Lorem ipsum dolor sit amet, consectetur dolor sit</li>
          <li>Lorem ipsum dolor sit amet, conse</li>
        </ul>
      </article>
    </section>
  </main>
</body>
</html>
```